Poster Design for a tea beverage brand - seasonal product "Lychee Rose Tea"

We're chain of bubble tea beverage stores, located mainly in New York, and we're looking for professional poster design for our new seasonal product - Lychee Rose Tea(Please note there's no boba in this product). Our brand spirit is to deliver the most authentic flavor of tea from Taiwan. We want the style of the poster to be lovely and energetic that targets at customers around 18-35 age group, both male and female. We would like to see an image of spring felling, expressing the freshness and tasty of our products. Attached are some posters, whose styles are similar to what we want. Also attached our current product photo and some similar product photos downloaded from website for your reference.

```html
<!DOCTYPE html>
<html lang="en">
<head>
<meta charset="utf-8">
<title>Lychee Rose Tea — Seasonal Poster</title>
<link href="https://fonts.googleapis.com/css2?family=Quicksand:wght@400;500&family=Pacifico&display=swap" rel="stylesheet">
<style>
  :root {
    --sand: #cfc49c;
    --sage: #8aa177;
    --moss: #6f8d62;
    --mauve: #8c6a72;
    --charcoal: #5a5a58;
    --honey: #e8c06c;
    --white: #ffffff;
    --cup-top: #f3dd8a;
    --cup-mid: #f2b531;
    --cup-low: #eaa52a;
    --splash: rgba(55, 62, 50, 0.55);
  }
  * { box-sizing: border-box; margin: 0; padding: 0; }
  html, body { width: 900px; height: 1200px; overflow: hidden; }
  body { font-family: "Quicksand", sans-serif; }

  .poster {
    position: relative;
    width: 900px;
    height: 1200px;
    overflow: hidden;
    background:
      radial-gradient(ellipse at 50% 45%, rgba(255,255,255,0.10), transparent 60%),
      linear-gradient(180deg, var(--sand) 0%, #b6b88c 25%, var(--sage) 45%, var(--moss) 62%, #8a8a6e 82%, var(--mauve) 100%);
  }

  .backdrop-texture {
    position: absolute;
    inset: 0;
    background:
      linear-gradient(90deg, rgba(255,255,255,0.18), transparent 12%, transparent 88%, rgba(255,255,255,0.18));
  }

  .splash {
    position: absolute;
    left: 140px;
    top: 620px;
    width: 620px;
    height: 320px;
    background: radial-gradient(ellipse at 50% 55%, var(--splash) 0%, rgba(55,62,50,0.25) 45%, transparent 70%);
  }

  .headline { position: absolute; inset: 0; }

  .flavor {
    position: absolute;
    left: 150px;
    width: 560px;
    font-weight: 400;
    font-size: 124px;
    line-height: 1;
    letter-spacing: -4px;
    color: var(--charcoal);
    white-space: nowrap;
  }
  .flavor--main { top: 148px; }
  .flavor--echo-1 { top: 244px; opacity: 0.45; }
  .flavor--echo-2 { top: 340px; opacity: 0.2; }
  .flavor--echo-3 { top: 436px; opacity: 0.08; }

  .accent {
    position: absolute;
    left: 335px;
    top: 222px;
    font-family: "Pacifico", cursive;
    font-size: 150px;
    line-height: 1;
    color: var(--honey);
    -webkit-text-stroke: 10px var(--white);
    paint-order: stroke fill;
    transform: rotate(-4deg);
  }

  .product-word {
    position: absolute;
    left: 226px;
    top: 398px;
    font-weight: 400;
    font-size: 310px;
    line-height: 1;
    letter-spacing: -6px;
    color: var(--white);
  }

  .drink-glow {
    position: absolute;
    left: 280px;
    top: 715px;
    width: 360px;
    height: 410px;
    background: radial-gradient(ellipse at 50% 50%, rgba(255,255,255,0.85) 40%, rgba(255,255,255,0) 70%);
    filter: blur(6px);
  }

  .drink-photo {
    position: absolute;
    left: 300px;
    top: 730px;
    width: 322px;
    height: 382px;
    clip-path: polygon(0 4%, 100% 4%, 92% 100%, 14% 100%);
    background: linear-gradient(180deg, var(--cup-top) 0%, #f4e0a6 18%, var(--cup-mid) 40%, var(--cup-low) 100%);
  }
</style>
</head>
<body>
  <main class="poster">
    <div class="backdrop-texture" role="img" aria-label="Soft painted brush texture in sand, sage and mauve tones"></div>
    <div class="splash" role="img" aria-label="Dark ink splash behind the drink"></div>

    <h1 class="headline">
      <span class="flavor flavor--main">LYCHEE</span>
      <span class="flavor flavor--echo-1" aria-hidden="true">LYCHEE</span>
      <span class="flavor flavor--echo-2" aria-hidden="true">LYCHEE</span>
      <span class="flavor flavor--echo-3" aria-hidden="true">LYCHEE</span>
      <span class="accent">Rose</span>
      <span class="product-word">Tea</span>
    </h1>

    <div class="drink-glow"></div>
    <div class="drink-photo" role="img" aria-label="Photo of an iced Lychee Rose Tea in a clear branded cup with ice cubes"></div>
  </main>
</body>
</html>
```